Lady Winnow's Cask Aged Heronfield Rum LABEL

Tallowbrook Distillery is looking for a label for our new product (Lady Winnow's Cask). This will be a barrel aged Rum that is distilled, bottled, and aged in small batches in Belmont, NC just outside of Charlotte, North Carolina. In the attached file (drink recipes) you will see the Product that we currently sell (Heronfield Rum). The new product does not have to be the same style, but we would like to maintain some brand relevance. There are some other attachments to give you an idea about the look of the company. Also attached is a picture of the dark rum in the bottle. This is what the label will go onto.

-The label will most likely be printed on craft paper stock.

Industry/Entity Type

It Company

Requirements
Must have
• We need the following in the new label
-Company Name= Tallowbrook Distillery
-Product name= Lady Winnow's Cask
-Product sub-name= Aged Heronfield Rum
-Product description= Distilled Bottled and Aged by Tallowbrook Distillery
Nice to have
• We would like to incorporate a rendering of Lady Winnow or just a crown. We think this is important because Charlotte, NC is named after her.

```html
<!DOCTYPE html>
<html lang="en">
<head>
<meta charset="utf-8">
<title>Lady Winnow's Cask – Aged Heronfield Rum Label</title>
<link rel="stylesheet" href="https://fonts.googleapis.com/css2?family=Bilbo+Swash+Caps&family=Arimo:wght@400;700&display=swap">
<style>
  :root {
    --label-black: #000000;
    --gold-light: #f6d27a;
    --gold-mid: #d9a84a;
    --gold-deep: #8a5a1c;
    --gold-text: #d9ae5c;
    --cream: #ffffff;
    --portrait-glow: #c98a4a;
    --portrait-dark: #3a1c10;
  }
  * { margin: 0; padding: 0; box-sizing: border-box; }
  html, body {
    width: 690px; height: 1200px; overflow: hidden;
    background: var(--label-black);
  }
  .label {
    position: relative; width: 690px; height: 1200px;
    background: var(--label-black);
  }
  .top-strip {
    position: absolute; left: 0; top: 0; width: 100%; height: 18px;
    background: linear-gradient(90deg, var(--gold-deep), var(--gold-light) 50%, var(--gold-deep));
  }
  .portrait-frame {
    position: absolute; left: 110px; top: 44px; width: 470px; height: 596px;
  }
  .product-name {
    position: absolute; left: 0; width: 100%; text-align: center;
    font-family: "Bilbo Swash Caps", serif;
    color: var(--gold-text); font-size: 92px; line-height: 1;
  }
  .product-name.line-one { top: 652px; }
  .product-name.line-two { top: 758px; }
  .rule {
    position: absolute; left: 0; width: 100%; height: 3px;
    background: linear-gradient(90deg, var(--gold-deep), var(--gold-light) 50%, var(--gold-deep));
  }
  .rule.upper { top: 862px; }
  .rule.lower { top: 934px; }
  .sub-name {
    position: absolute; top: 873px; left: 0; width: 100%; text-align: center;
    font-family: "Arimo", sans-serif; font-weight: 700;
    color: var(--cream); font-size: 46px; line-height: 52px;
  }
  .company-name {
    position: absolute; top: 1018px; left: 0; width: 100%; text-align: center;
    font-family: "Bilbo Swash Caps", serif;
    color: var(--gold-text); font-size: 46px; line-height: 1;
  }
  .description-band {
    position: absolute; left: 0; top: 1136px; width: 100%; height: 50px;
    background: linear-gradient(90deg, var(--gold-deep), var(--gold-light) 45%, var(--gold-mid) 70%, var(--gold-deep));
    display: flex; align-items: center; justify-content: center;
    font-family: "Arimo", sans-serif; color: var(--label-black);
    font-size: 27px;
  }
</style>
</head>
<body>
<main class="label">
  <div class="top-strip"></div>

  <svg class="portrait-frame" viewBox="0 0 470 596" xmlns="http://www.w3.org/2000/svg">
    <defs>
      <linearGradient id="frameGold" x1="0" y1="0" x2="1" y2="1">
        <stop offset="0" stop-color="#f6d27a"/>
        <stop offset="0.45" stop-color="#a86a24"/>
        <stop offset="0.7" stop-color="#f2c66c"/>
        <stop offset="1" stop-color="#6e4212"/>
      </linearGradient>
      <radialGradient id="portraitFill" cx="0.5" cy="0.45" r="0.6">
        <stop offset="0" stop-color="#e0a868"/>
        <stop offset="0.5" stop-color="#8a4a22"/>
        <stop offset="1" stop-color="#3a1c10"/>
      </radialGradient>
    </defs>
    <ellipse cx="235" cy="298" rx="222" ry="284" fill="url(#frameGold)"/>
    <ellipse cx="235" cy="298" rx="196" ry="258" fill="#5a3212"/>
    <ellipse cx="235" cy="298" rx="190" ry="252" fill="url(#portraitFill)"
             role="img" aria-label="Illustrated portrait of Lady Winnow in a red ermine-trimmed robe"/>
  </svg>

  <h1 class="product-name line-one">Lady Winnow's</h1>
  <div class="product-name line-two">Cask</div>

  <div class="rule upper"></div>
  <h2 class="sub-name">Aged Heronfield Rum</h2>
  <div class="rule lower"></div>

  <p class="company-name">Tallowbrook Distillery</p>

  <p class="description-band">Distilled Bottled and Aged by Tallowbrook Distillery</p>
</main>
</body>
</html>
```